Handmade candle business in melbourne requiring assistance with designing classy labels

My business name is Wick and Willow.
I specialise in making handmade candles, i'm based in Melbourne.
My moto is "Delicately hand poured and infused by me...for you"
wickwillow@mailbox-demo.net
0487 913 072

I need some assistance with designing my labels for my glass candles
I really like earthy colours and nothing too bright, but I want it to look classy and elegant and something that stands out from other homemade candle businesses.
I have attached a sample of a design that appeals to me but open to suggestions.

```html
<!DOCTYPE html>
<html lang="en">
<head>
<meta charset="UTF-8">
<title>Wick and Willow — Candle Label</title>
<link rel="stylesheet" href="https://fonts.googleapis.com/css2?family=Alex+Brush&family=Crimson+Pro:ital,wght@1,400&display=swap">
<style>
  :root {
    --page-bg: #ffffff;
    --label-base: #f4e5d6;
    --label-light: #fcf3ea;
    --ring: #8c2f22;
    --ink: #1a1512;
    --tagline: #3a3330;
    --contact: #8c2f22;
  }
  html, body {
    margin: 0;
    padding: 0;
    width: 1200px;
    height: 1200px;
    overflow: hidden;
    background: var(--page-bg);
  }
  .canvas {
    position: relative;
    width: 1200px;
    height: 1200px;
  }
  .label-art {
    position: absolute;
    left: 0;
    top: 0;
  }
  .label-text {
    position: absolute;
    left: 0;
    width: 1200px;
    text-align: center;
    margin: 0;
  }
  .brand-name {
    top: 462px;
    font-family: "Alex Brush", cursive;
    font-weight: 400;
    font-size: 76px;
    line-height: 1;
    color: var(--ink);
  }
  .tagline {
    top: 598px;
    font-family: "Crimson Pro", serif;
    font-style: italic;
    font-size: 36px;
    line-height: 48px;
    color: var(--tagline);
  }
  .contact {
    top: 740px;
    font-family: "Crimson Pro", serif;
    font-style: italic;
    font-size: 29px;
    line-height: 44px;
    color: var(--contact);
  }
</style>
</head>
<body>
<main class="canvas">
  <svg class="label-art" width="1200" height="1200" viewBox="0 0 1200 1200">
    <defs>
      <radialGradient id="label-glow" cx="50%" cy="50%" r="50%">
        <stop offset="0%" stop-color="var(--label-light)"/>
        <stop offset="100%" stop-color="var(--label-base)"/>
      </radialGradient>
    </defs>
    <circle class="label-disc" cx="600" cy="601" r="338" fill="url(#label-glow)"
            role="img" aria-label="Soft sunburst ray pattern in cream and pale beige"/>
    <circle class="label-ring" cx="600" cy="601" r="312" fill="none" stroke="var(--ring)" stroke-width="4.5"/>
  </svg>

  <h1 class="label-text brand-name">Wick and Willow</h1>
  <p class="label-text tagline">Delicately hand poured and<br>infused by me...for you</p>
  <p class="label-text contact">wickwillow@mailbox-demo.net<br>0487 913 072</p>
</main>
</body>
</html>
```